Calvexa, Business marketing Flyer

I need a Professional full page flyer displaying a telephone that my company uses.
Calvexa’s Cloud Based communication offers unlimited local and long distance calling, and unlimited call paths so your customers never receive a busy signal. With the use of a cell phone application recieve calls to your extension, or make outbound calls displaying your business telephone number. Manage your entire phone system through an online portal, record your calls, and receive call reporting. Our Virtual Faxing brings faxing to a whole new level. Send and receive your faxes directly through an email. Interested in a custom message/music to inform your clients of your services while they wait on hold? Calvexa has you covered there too. Find out today how you can save upwards of 37% on your monthly telecommunications expenses. I don't want there to be too much verbiage on the flyer but get the point across as to what it is that we do.

Target Market(s)

All Small-Medium size Businesses

Industry/Entity Type

Voip

Requirements
Must have
• 3 major bullet points
• Cut Costs
• Innovative Features
• Easy Set Up
• Save Upwards of 37% on your monthly telecommunications costs
• Keep your main telephone number
• Hands on Support
• 866-491-7305

```html
<!DOCTYPE html>
<html lang="en">
<head>
<meta charset="utf-8">
<title>Calvexa – Cloud Based Business Phone Flyer</title>
<link href="https://fonts.googleapis.com/css2?family=Montserrat:wght@300;400;700;800;900&display=swap" rel="stylesheet">
<style>
  :root {
    --navy: #1f2a6b;
    --navy-mid: #27367f;
    --navy-deep: #18205a;
    --mist: #e6e6e8;
    --paper: #ffffff;
    --ink: #555558;
    --ink-dark: #444446;
    --stage: #eceae6;
    --photo-warm: #8a5a36;
    --photo-dark: #3a2a22;
    --device: #2b3038;
  }
  * { margin: 0; padding: 0; box-sizing: border-box; }
  html, body {
    width: 1200px; height: 1200px; overflow: hidden;
    background: var(--stage);
    font-family: "Montserrat", sans-serif;
  }
  .flyer {
    position: absolute;
    left: 197px; top: 30px;
    width: 951px; height: 1344px;
    transform: scale(0.848);
    transform-origin: 0 0;
    background: var(--paper);
    overflow: hidden;
    box-shadow: 0 6px 22px rgba(0,0,0,0.18);
  }
  .flyer-shapes { position: absolute; inset: 0; }
  .abs { position: absolute; }

  .brand {
    left: 50px; top: 78px;
    display: flex; align-items: center; gap: 22px;
    font-weight: 800; font-size: 96px; letter-spacing: 2px;
    color: var(--navy); line-height: 1;
  }
  .brand-square { width: 70px; height: 70px; background: var(--navy); }

  .headline { left: 51px; top: 246px; color: var(--navy); }
  .headline-lead { font-weight: 300; font-size: 37px; color: var(--ink); letter-spacing: 1px; line-height: 1.1; }
  .headline-main { font-weight: 900; font-size: 50px; line-height: 1.04; margin-top: 2px; }

  .section-title { left: 40px; top: 648px; }
  .section-kicker { font-weight: 300; font-size: 55px; color: var(--ink); line-height: 1; }
  .section-main { font-weight: 900; font-size: 39px; color: var(--navy); line-height: 1.1; margin-top: 6px; }

  .body-copy {
    left: 40px; top: 763px; width: 548px;
    font-size: 15.3px; line-height: 19.3px; color: var(--ink); font-weight: 400;
  }

  .feature { top: 980px; width: 150px; }
  .feature-icon {
    width: 113px; height: 113px; background: var(--navy);
    display: flex; align-items: center; justify-content: center;
  }
  .feature-label { margin-top: 8px; font-size: 19px; line-height: 23px; color: var(--ink); letter-spacing: 0.5px; }

  .savings { left: 40px; top: 1158px; }
  .savings-main { font-weight: 900; font-size: 35px; color: var(--navy); letter-spacing: 0.5px; line-height: 1.1; }
  .savings-sub { font-size: 18.5px; color: var(--ink); letter-spacing: 1.2px; margin-top: 8px; }

  .support-bar { left: 40px; top: 1254px; width: 860px; height: 54px; }
  .support-label {
    position: absolute; left: 45px; top: 0; height: 54px;
    display: flex; align-items: center;
    color: var(--paper); font-weight: 800; font-size: 26px; letter-spacing: 0.5px;
  }
  .support-phone {
    position: absolute; left: 458px; top: 0; height: 54px;
    display: flex; align-items: center;
    color: var(--ink-dark); font-weight: 800; font-size: 42px; letter-spacing: 2px;
  }
</style>
</head>
<body>
<main class="flyer">
  <svg class="flyer-shapes" viewBox="0 0 951 1344" width="951" height="1344">
    <defs>
      <linearGradient id="photoTone" x1="0" y1="0" x2="1" y2="1">
        <stop offset="0" stop-color="var(--photo-dark)"/>
        <stop offset="0.55" stop-color="var(--photo-warm)"/>
        <stop offset="1" stop-color="var(--photo-dark)"/>
      </linearGradient>
      <linearGradient id="deviceTone" x1="0" y1="0" x2="1" y2="1">
        <stop offset="0" stop-color="#3b414b"/>
        <stop offset="1" stop-color="var(--device)"/>
      </linearGradient>
    </defs>
    <!-- light upper field -->
    <polygon points="0,0 755,0 878,77 275,441 165,506 0,598" fill="var(--mist)"/>
    <!-- top right corner wedge -->
    <polygon points="755,0 951,0 951,31 878,77" fill="var(--navy)"/>
    <!-- accent lines -->
    <line x1="430" y1="0" x2="721" y2="168" stroke="var(--navy)" stroke-width="2"/>
    <line x1="0" y1="411" x2="165" y2="506" stroke="var(--navy)" stroke-width="2"/>
    <line x1="0" y1="243" x2="40" y2="263" stroke="#9a9a9e" stroke-width="2"/>
    <line x1="265" y1="396" x2="305" y2="416" stroke="#9a9a9e" stroke-width="2"/>
    <!-- small wedge beside photo -->
    <polygon points="165,506 275,441 275,581" fill="var(--navy)"/>
    <!-- photo area -->
    <polygon points="275,441 721,168 878,77 878,616 615,769 275,581" fill="url(#photoTone)"
             role="img" aria-label="Photo: smiling woman talking on a mobile phone at a café table with a coffee cup"/>
    <!-- navy block lower right -->
    <polygon points="615,769 878,616 878,926 775,986 615,986" fill="var(--navy-mid)"/>
    <polygon points="615,769 878,926 775,986 615,986" fill="var(--navy)"/>
    <polygon points="615,880 775,986 615,986" fill="var(--navy-deep)"/>
    <!-- desk phone product -->
    <path d="M560,1200 L610,1000 L870,985 L865,1195 Z" fill="url(#deviceTone)"
          role="img" aria-label="Product photo: business IP desk phone with colour touchscreen and keypad"/>
    <!-- support bar -->
    <g transform="translate(40,1254)">
      <polygon points="0,0 390,0 412,27 390,54 0,54" fill="var(--navy)"/>
      <line x1="390" y1="1" x2="860" y2="1" stroke="var(--navy)" stroke-width="3"/>
      <line x1="390" y1="53" x2="860" y2="53" stroke="var(--navy)" stroke-width="3"/>
    </g>
  </svg>

  <div class="abs brand"><span>CALVEXA</span><span class="brand-square"></span></div>

  <div class="abs headline">
    <div class="headline-lead">KEEP YOUR MAIN</div>
    <div class="headline-main">TELEPHONE<br>NUMBER</div>
  </div>

  <div class="abs section-title">
    <div class="section-kicker">CALVEXA’S</div>
    <div class="section-main">CLOUD BASED</div>
  </div>

  <p class="abs body-copy">Calvexa’s Cloud Based communication offers unlimited local and long distance calling, and unlimited call paths so your customers never receive a busy signal. With the use of a cell phone application recieve calls to your extension, or make outbound calls displaying your business telephone number. Manage your entire phone system through an online portal, record your calls, and receive call reporting. Our Virtual Faxing brings faxing to a whole new level. Send and receive your faxes directly through an email. Interested in a custom message/music to inform your clients of your services while they wait on hold? Calvexa has you covered there too.</p>

  <div class="abs feature" style="left:40px">
    <div class="feature-icon">
      <span style="color:#fff;font-weight:900;font-size:70px;line-height:1">$</span>
    </div>
    <div class="feature-label">Cut Costs</div>
  </div>
  <div class="abs feature" style="left:242px">
    <div class="feature-icon">
      <svg width="60" height="76" viewBox="0 0 60 76" fill="none" stroke="#fff" stroke-width="3">
        <path d="M18,52 C8,45 4,36 4,28 A26,26 0 0 1 56,28 C56,36 52,45 42,52 Z"/>
        <circle cx="30" cy="27" r="9"/>
        <circle cx="30" cy="27" r="15" stroke-dasharray="4 4"/>
        <line x1="20" y1="58" x2="40" y2="58"/>
        <line x1="22" y1="64" x2="38" y2="64"/>
        <line x1="26" y1="70" x2="34" y2="70"/>
      </svg>
    </div>
    <div class="feature-label">Innovative<br>Features</div>
  </div>
  <div class="abs feature" style="left:445px">
    <div class="feature-icon">
      <svg width="60" height="76" viewBox="0 0 60 76" fill="#fff">
        <rect x="6" y="4" width="26" height="12" rx="2" transform="rotate(-20 19 10)"/>
        <rect x="20" y="12" width="6" height="30" transform="rotate(-20 23 27)"/>
        <path d="M18,44 C22,40 32,38 40,42 L50,52 C52,58 48,70 38,72 L28,70 C22,66 18,58 18,44 Z"/>
      </svg>
    </div>
    <div class="feature-label">Easy Set Up</div>
  </div>

  <div class="abs savings">
    <div class="savings-main">SAVE UPWARDS OF 37%</div>
    <div class="savings-sub">ON YOUR MONTHLY TELECOMMUNICATIONS COSTS</div>
  </div>

  <div class="abs support-bar">
    <span class="support-label">HANDS ON SUPPORT</span>
    <span class="support-phone">866-491-7305</span>
  </div>
</main>
</body>
</html>
```